Change of trading name, rebrand

existing website to be updated with new theme and logo. existing website is
www.brackenridgeworks.com.au
Industry/Entity Type
Construction
Coding
Coded - Design and coding required
Number of Pages Required
5+ page
Requirements
Must have
- be mobile phone friendly

```html
<!DOCTYPE html>
<html lang="en">
<head>
<meta charset="utf-8">
<meta name="viewport" content="width=device-width, initial-scale=1">
<title>BRW Plant Hire</title>
<link href="https://fonts.googleapis.com/css2?family=Poppins:wght@400;500;600;700;800&display=swap" rel="stylesheet">
<style>
:root{
  --navy:#2e3172;
  --navy-deep:#23265a;
  --navy-soft:#4a4f95;
  --ink:#232328;
  --card:#2f3036;
  --text:#55565e;
  --muted:#8a8b93;
  --line:#e3e4ea;
  --white:#ffffff;
  --photo-sky:#b9c2d6;
  --photo-earth:#a88c6a;
  --photo-machine:#d8742f;
}
*{box-sizing:border-box;margin:0;padding:0}
html,body{width:1200px;height:4260px;overflow:hidden}
body{font-family:"Poppins",Arial,sans-serif;color:var(--ink);background:var(--white);position:relative}
.abs{position:absolute}
.photo{position:absolute;background:linear-gradient(160deg,var(--photo-sky) 0%,#9aa6bf 45%,var(--photo-earth) 100%)}
.photo.machine{background:linear-gradient(150deg,var(--photo-sky) 0%,#c9b79f 50%,var(--photo-machine) 100%)}
.photo.water{background:linear-gradient(160deg,#c4cbd6 0%,#7f8fa3 55%,#5d6b55 100%)}

/* header */
.site-header{left:0;top:0;width:1200px;height:130px}
.brand{left:80px;top:14px;display:flex;align-items:center;gap:10px}
.brand-mark{width:22px;height:22px;background:var(--navy)}
.brand-name{font-weight:800;font-size:30px;color:var(--navy);letter-spacing:1px}
.brand-sub{left:112px;top:62px;font-size:11px;font-weight:600;color:var(--navy);letter-spacing:3px}
.contact-bar{right:80px;top:12px;display:flex;gap:34px}
.contact-item{display:flex;gap:10px;align-items:flex-start}
.contact-item svg{width:26px;height:26px;flex:none}
.contact-item b{display:block;font-size:12px;color:var(--ink)}
.contact-item span{font-size:12px;color:var(--text)}
.main-nav{left:125px;top:90px;display:flex;gap:24px;font-size:13px;font-weight:500;white-space:nowrap}
.main-nav a{color:var(--ink);text-decoration:none}
.social{display:flex;gap:6px}
.social i{display:block;width:26px;height:26px;background:var(--navy)}
.header-social{left:770px;top:86px}
.search{left:888px;top:86px;width:190px;height:28px;border:1px solid var(--line);font-size:12px;color:var(--muted);padding:5px 10px}
.search-btn{left:1046px;top:86px;width:32px;height:28px;background:var(--navy)}

/* hero */
.hero{left:0;top:130px;width:1200px;height:560px;background:linear-gradient(100deg,var(--navy-deep) 0%,var(--navy-soft) 55%,#9ea6c6 100%);overflow:hidden}
.hero-photo{left:560px;top:20px;width:560px;height:420px;border-radius:20px;background:linear-gradient(150deg,#c7cede 0%,#8b93ae 50%,var(--photo-machine) 100%);opacity:.85}
.hero-title{left:100px;top:300px;width:620px;font-size:40px;line-height:50px;font-weight:700;color:var(--white);border-left:4px solid var(--white);padding-left:16px;white-space:nowrap}
.hero-text{left:120px;top:418px;width:420px;font-size:13px;line-height:20px;color:#d9dcec}
.btn-dark{display:inline-block;background:var(--ink);color:var(--white);font-size:14px;font-weight:500;padding:10px 24px;border-radius:22px}
.hero-cta{left:100px;top:482px}
.hero-video{left:236px;top:484px;display:flex;align-items:center;gap:10px;color:var(--white);font-weight:600;font-size:16px}
.hero-video i{width:38px;height:38px;border:2px solid var(--white);border-radius:50%;display:flex;align-items:center;justify-content:center}
.hero-wave{left:0;top:611px;width:1200px;height:80px}

/* about */
.about-kicker{left:88px;top:800px;font-size:15px;font-weight:600}
.about-title{left:88px;top:822px;width:500px;font-size:32px;line-height:40px;font-weight:700;color:var(--navy)}
.about-text{left:88px;top:912px;width:470px;font-size:12px;line-height:19px;color:var(--text)}
.learn-more{left:88px;top:1112px;font-size:12px;font-weight:600}
.about-photo-a{left:608px;top:780px;width:200px;height:370px;border-radius:10px}
.about-photo-b{left:818px;top:780px;width:290px;height:370px;border-radius:10px}
.badge{left:760px;top:880px;width:110px;height:110px;border-radius:50%;background:var(--white);box-shadow:0 4px 14px rgba(0,0,0,.15);text-align:center;padding-top:24px}
.badge b{display:block;font-size:34px;line-height:36px;font-weight:700}
.badge span{font-size:8px;font-weight:600;letter-spacing:1px}

/* stats */
.stats{left:80px;top:1210px;width:1040px;display:flex;justify-content:space-between}
.stat{width:180px}
.stat svg{width:58px;height:58px;display:block;margin-bottom:18px}
.stat b{display:block;font-size:48px;line-height:50px;font-weight:700}
.stat span{display:block;margin-top:8px;font-size:12px;font-weight:500;letter-spacing:.5px;text-transform:uppercase;line-height:16px}

/* hire */
.hire-band{left:0;top:1475px;width:1060px;height:530px;background:linear-gradient(110deg,var(--navy-deep),var(--navy-soft))}
.hire-photo{left:180px;top:1570px;width:365px;height:445px;border-radius:6px}
.hire-title{left:592px;top:1640px;font-size:34px;font-weight:700;color:var(--white)}
.hire-text{left:592px;top:1690px;width:400px;font-size:12px;line-height:19px;color:#dde0ef}
.hire-cta{left:592px;top:1888px}
.hire-cta .btn-dark{padding:10px 22px}
.side-tab{left:1060px;top:1475px;width:140px;height:560px;background:var(--card)}
.side-tab-label{left:1060px;top:1640px;width:140px;height:260px;display:flex;align-items:center;justify-content:center}
.side-tab-label span{transform:rotate(-90deg);white-space:nowrap;color:var(--white);font-size:30px;font-weight:700}
.side-arrow{left:1110px;top:1515px}
.side-photo{left:1060px;top:1875px;width:140px;height:160px}

/* projects */
.section-title{left:0;width:1200px;text-align:center;font-size:34px;font-weight:700;color:var(--navy)}
.section-sub{left:0;width:1200px;text-align:center;font-size:13px;color:var(--text)}
.proj{width:322px;height:355px}
.proj-card{left:440px;top:2560px;width:322px;height:360px;background:var(--navy);color:var(--white);display:flex;flex-direction:column;justify-content:center;align-items:center;text-align:center}
.proj-card b{font-size:18px;font-weight:700}
.proj-card span{font-size:11px;line-height:17px;margin-top:6px;color:#d4d7ea}
.projects-cta{left:0;width:1200px;top:2955px;text-align:center}
.projects-cta .btn-dark{border-radius:0;padding:10px 26px}

/* quote */
.quote-card{left:85px;top:3065px;width:445px;height:540px;background:var(--card);padding:30px 50px}
.quote-card h2{color:var(--white);font-size:34px;line-height:40px;font-weight:700}
.field{display:block;width:100%;height:38px;border:1px solid #55565e;background:#3a3b42;color:#b9bac2;font-size:11px;padding:0 14px;line-height:38px;margin-top:14px}
.field.area{height:90px;line-height:34px}
.submit{margin-top:20px;height:42px;background:var(--navy);color:var(--white);font-size:13px;font-weight:600;text-align:center;line-height:42px;border-radius:8px}
.quote-brand{left:640px;top:3100px}
.quote-brand .brand-name{font-size:54px;color:var(--ink)}
.quote-brand small{display:block;font-size:13px;font-weight:600;letter-spacing:5px}
.info{left:640px;display:flex;gap:16px;align-items:flex-start}
.info svg{width:30px;height:30px;flex:none}
.info b{display:block;font-size:20px;color:var(--navy);font-weight:700}
.info span{font-size:13px;color:var(--text)}
.quote-social{left:640px;top:3470px}
.quote-social i{width:34px;height:34px;border-radius:50%}
.quote-deco{left:820px;top:3320px;width:380px;height:300px;background:linear-gradient(160deg,rgba(46,49,114,0) 0%,rgba(46,49,114,.08) 100%)}

/* partners */
.partners{left:90px;top:3705px;width:1020px;display:flex;justify-content:space-between;align-items:center}
.partners i{display:block;height:40px;background:#c9cad2}

/* footer */
.site-footer{left:0;top:3820px;width:1200px;height:440px;background:var(--navy)}
.footer-brand{left:100px;top:3960px}
.footer-brand .brand-name{color:var(--white);font-size:54px}
.footer-brand small{display:block;color:var(--white);font-size:13px;font-weight:600;letter-spacing:5px}
.footer-col{top:3910px;color:var(--white)}
.footer-col h3{font-size:20px;font-weight:700;margin-bottom:14px}
.footer-col a{display:block;color:var(--white);text-decoration:none;font-size:13px;line-height:22px}
.footer-col p{font-size:12px;line-height:22px;display:flex;gap:8px;align-items:center}
.footer-photo{left:850px;top:3860px;width:330px;height:300px;border-radius:12px;background:linear-gradient(150deg,rgba(255,255,255,.05),var(--photo-machine));opacity:.9}
.copyright{left:0;top:4210px;width:1200px;height:50px;border-top:1px solid rgba(255,255,255,.2);text-align:center;color:var(--white);font-size:12px;line-height:50px}
</style>
</head>
<body>

<header class="abs site-header">
  <div class="abs brand"><div class="brand-mark"></div><div class="brand-name">BRW</div></div>
  <div class="abs brand-sub">PLANT HIRE</div>
  <div class="abs contact-bar">
    <div class="contact-item">
      <svg viewBox="0 0 24 24"><path d="M12 2a7 7 0 0 0-7 7c0 5 7 13 7 13s7-8 7-13a7 7 0 0 0-7-7zm0 9.5A2.5 2.5 0 1 1 12 6.5a2.5 2.5 0 0 1 0 5z" fill="#2e3172"/></svg>
      <div><b>Location</b><span>18 Gumtree Rd, Yatala QLD 4207</span></div>
    </div>
    <div class="contact-item">
      <svg viewBox="0 0 24 24"><path d="M6.6 10.8a15 15 0 0 0 6.6 6.6l2.2-2.2a1 1 0 0 1 1-.25 11.4 11.4 0 0 0 3.6.6 1 1 0 0 1 1 1V20a1 1 0 0 1-1 1A17 17 0 0 1 3 4a1 1 0 0 1 1-1h3.5a1 1 0 0 1 1 1c0 1.250.2 2.45.6 3.6a1 1 0 0 1-.25 1z" fill="#2e3172"/></svg>
      <div><b>Phone</b><span>1300 555 010</span></div>
    </div>
    <div class="contact-item">
      <svg viewBox="0 0 24 24"><rect x="6" y="2" width="12" height="20" rx="2" fill="#2e3172"/><rect x="8" y="4" width="8" height="13" fill="#fff"/></svg>
      <div><b>Mobile</b><span>04 0000 0148</span></div>
    </div>
  </div>
  <nav class="abs main-nav"><a href="#">Home</a><a href="#">About Us</a><a href="#">Plant Hire</a><a href="#">Major Project Snapshot</a><a href="#">Policies</a><a href="#">Jobs</a></nav>
  <div class="abs social header-social"><i></i><i></i><i></i></div>
  <div class="abs search">Search...</div>
  <div class="abs search-btn"></div>
</header>

<section class="abs hero">
  <div class="abs hero-photo" role="img" aria-label="Orange excavator on a work site"></div>
</section>
<h1 class="abs hero-title">Your Trusted Partner in<br>Heavy Equipment Hire</h1>
<p class="abs hero-text">BRW Plant Hire delivers quality machinery and expert service for efficient, safe projects. Trust us for all your equipment needs.</p>
<div class="abs hero-cta"><span class="btn-dark">Contact Us</span></div>
<div class="abs hero-video">Video <i><svg width="12" height="14" viewBox="0 0 12 14"><path d="M0 0l12 7-12 7z" fill="#fff"/></svg></i></div>
<svg class="abs hero-wave" viewBox="0 0 1200 80" preserveAspectRatio="none"><path d="M0 40 Q300 0 600 30 T1200 20 V80 H0z" fill="#fff"/></svg>

<section>
  <div class="abs about-kicker">BRW Heavy Equipment Hire</div>
  <h2 class="abs about-title">Committed to superior qualityplant hire services.</h2>
  <p class="abs about-text">Brackenridge Heavy Equipment Hire specialises in the hire of heavy earthmoving, mining and construction machines with specialised attachments and tooling. Our array of machines and attachments is second to none and we have one of the largest fleet fleets available in South East Queensland. If you need a machine, excavator or attachment, BRW is the crew to call. You can find all you require here at our yard, and we provide excellent operators and quality machines across all models and brands to help you achieve maximum up-time.</p>
  <div class="abs learn-more">Learn More ›</div>
  <div class="photo about-photo-a" role="img" aria-label="Site worker in hard hat reviewing plans"></div>
  <div class="photo machine about-photo-b" role="img" aria-label="Yellow excavator on a job site"></div>
  <div class="abs badge"><b>20+</b><span>YEARS OF EXPERIENCE</span></div>
</section>

<section class="abs stats">
  <div class="stat">
    <svg viewBox="0 0 58 58" fill="none" stroke="#232328" stroke-width="2.5"><circle cx="29" cy="16" r="9"/><path d="M12 54v-8a17 17 0 0 1 34 0v8"/></svg>
    <b>20+</b><span>Years of<br>Experience</span>
  </div>
  <div class="stat">
    <svg viewBox="0 0 58 58" fill="none" stroke="#232328" stroke-width="2.5"><path d="M6 44h30v-12H18l-6 6H6z"/><path d="M30 32l10-16 12 8-6 14"/><circle cx="12" cy="48" r="4"/><circle cx="30" cy="48" r="4"/></svg>
    <b>100+</b><span>Machines<br>in Fleet</span>
  </div>
  <div class="stat">
    <svg viewBox="0 0 58 58" fill="none" stroke="#232328" stroke-width="2.5"><rect x="10" y="8" width="38" height="42" rx="3"/><path d="M18 20h22M18 29h22M18 38h14"/></svg>
    <b>50+</b><span>One of QLD's<br>Largest Suppliers</span>
  </div>
  <div class="stat">
    <svg viewBox="0 0 58 58" fill="none" stroke="#232328" stroke-width="2.5"><path d="M4 16h30v24H4zM34 24h12l8 8v8H34z"/><circle cx="14" cy="44" r="4"/><circle cx="44" cy="44" r="4"/></svg>
    <b>100+</b><span>Onsite<br>Servicing</span>
  </div>
  <div class="stat">
    <svg viewBox="0 0 58 58" fill="none" stroke="#232328" stroke-width="2.5"><path d="M10 48L40 18M18 10l30 30M40 18l8-8 4 4-8 8M10 48l-4 4"/></svg>
    <b>30+</b><span>Custom Machine<br>Attachments</span>
  </div>
</section>

<section>
  <div class="abs hire-band"></div>
  <div class="photo machine hire-photo" role="img" aria-label="Orange long-reach excavator at a quarry"></div>
  <h2 class="abs hire-title">Excavar Hire</h2>
  <p class="abs hire-text">With one of the largest fleet of excavators for hire in South East Queensland, BRW Heavy Equipment has an excavator to suit your project. Our range covers mini diggers through to large tracked units, with long-reach, tilt and specialised buckets available. From site preparation and trenching to demolition and dredging, our machines come well maintained and ready to work, backed by fast delivery and experienced onsite support.</p>
  <div class="abs hire-cta"><span class="btn-dark">Learn More ›</span></div>
  <div class="abs side-tab"></div>
  <svg class="abs side-arrow" width="40" height="20" viewBox="0 0 40 20"><path d="M0 10h36M28 2l8 8-8 8" stroke="#fff" stroke-width="2.5" fill="none"/></svg>
  <div class="abs side-tab-label"><span>Dump Trucks</span></div>
  <div class="photo machine side-photo" role="img" aria-label="Articulated dump truck"></div>
</section>

<section>
  <h2 class="abs section-title" style="top:2080px">Major Project Snapshot</h2>
  <p class="abs section-sub" style="top:2132px">We're incredibly proud of our major project experience.</p>
  <div class="photo machine proj" style="left:100px;top:2185px" role="img" aria-label="Excavators working on an earthworks site"></div>
  <div class="photo water proj" style="left:440px;top:2185px" role="img" aria-label="Long-reach excavator on a floating barge"></div>
  <div class="photo machine proj" style="left:778px;top:2185px" role="img" aria-label="Orange excavator on a cleared site"></div>
  <div class="photo machine proj" style="left:100px;top:2560px;height:360px" role="img" aria-label="Yellow excavator loading material"></div>
  <div class="abs proj-card"><b>Karrabin, Westline Rail</b><span>Client - Rail Upgrade<br>Commencement Year - 2018</span></div>
  <div class="photo machine proj" style="left:778px;top:2560px;height:360px" role="img" aria-label="Excavator working on a rail corridor"></div>
  <div class="abs projects-cta"><span class="btn-dark">View More Projects</span></div>
</section>

<section>
  <div class="abs quote-card">
    <h2>Contact us today for a FREE QUOTE</h2>
    <div style="margin-top:22px">
      <span class="field">Name *</span>
      <span class="field">Email *</span>
      <span class="field">Phone *</span>
      <span class="field area">Enquiry</span>
      <div class="submit">Submit Now</div>
    </div>
  </div>
  <div class="abs quote-deco" role="img" aria-label="Faint excavator line drawing"></div>
  <div class="abs quote-brand"><div class="brand-name">BRW</div><small>PLANT HIRE</small></div>
  <div class="abs info" style="top:3270px">
    <svg viewBox="0 0 24 24"><path d="M12 2a7 7 0 0 0-7 7c0 5 7 13 7 13s7-8 7-13a7 7 0 0 0-7-7zm0 9.5A2.5 2.5 0 1 1 12 6.5a2.5 2.5 0 0 1 0 5z" fill="#2e3172"/></svg>
    <div><b>Head Office:</b><span>18 Gumtree Rd, Yatala QLD 4207</span></div>
  </div>
  <div class="abs info" style="top:3370px">
    <svg viewBox="0 0 24 24"><path d="M6.6 10.8a15 15 0 0 0 6.6 6.6l2.2-2.2a1 1 0 0 1 1-.25 11.4 11.4 0 0 0 3.6.6 1 1 0 0 1 1 1V20a1 1 0 0 1-1 1A17 17 0 0 1 3 4a1 1 0 0 1 1-1h3.5a1 1 0 0 1 1 1c0 1.25.2 2.45.6 3.6a1 1 0 0 1-.25 1z" fill="#2e3172"/></svg>
    <div><b>Phone</b><span>1300 555 010</span></div>
  </div>
  <div class="abs social quote-social"><i></i><i></i><i></i><i></i></div>
</section>

<section class="abs partners" aria-label="Partners">
  <i style="width:150px"></i><i style="width:110px"></i><i style="width:120px"></i><i style="width:130px"></i><i style="width:150px"></i><i style="width:120px"></i>
</section>

<footer>
  <div class="abs site-footer"></div>
  <div class="abs footer-photo" role="img" aria-label="Yellow backhoe loader"></div>
  <div class="abs footer-brand"><div class="brand-name">BRW</div><small>PLANT HIRE</small></div>
  <div class="abs footer-col" style="left:410px">
    <h3>Quick links</h3>
    <a href="#">Home</a><a href="#">About Us</a><a href="#">Plant hire</a><a href="#">Major Project Snapshot</a><a href="#">Policies</a><a href="#">Jobs</a><a href="#">Contact Us</a>
  </div>
  <div class="abs footer-col" style="left:640px">
    <h3>Contact</h3>
    <p>☎ 1300 555 010</p>
    <p>▯ 04 0000 0148</p>
    <p>✉ www.brackenridgeworks.com.au</p>
    <p>⌖ 18 Gumtree Rd, Yatala QLD 4207</p>
  </div>
  <div class="abs copyright">©2024 BRW PlantHire</div>
</footer>

</body>
</html>
```